New solo practice law firm is looking for an elegant, professional, and interactive web design

I need a web design and developer for a new small law firm in Sacramento, California called Dorian Kessly Law, A Professional Corporation. I am a trial lawyer who represents average people facing difficult litigation disputes, including criminal defense as a former prosecutor and civil litigation as a civil litigator. Criminal defense includes domestic violence, battery, assault, drug possession, theft, DUI, etc. Civil litigation includes business disputes, property disputes, employment disputes, family law disputes, and immigration issues. I would like to see web designs that incorporate my logo and use the logo's navy blue and gold colors. I have uploaded the files of my logo to this brief. Please only use the navy blue and gold version. Overall, I want the design to look firm, professional, and elegant.

I plan on having the following pages on my website: (1) Home, (2) Dorian Kessly, (3) Practice Areas, (4) Insights, (5) Contact. I've hand drawn a preliminary sketch concept of what I envision the home page's layout to look like (attached with a text version). I would like your design to keep a similar layout for the homepage and incorporate my logo's colors within it but I am open to creative layout alternatives/ideas. I would like the other pages to have a similar look and feel as the home page. Some of the areas currently in my sketch do not have the full text. You can insert other text for now and I will provide the winner the full text.

In terms of the pictures on the website, I enjoy images of courthouses, columns (example attached but I cannot use this one), and, if possible, images from Sacramento, CA in my background (headshot attached). A plus would be live images that move and also sections of the webpage moving in the viewers view as they scroll down on the page. Also, it would be great to have my logo act as the tab for the website. I can provide other versions of the logo if needed.

I look forward to seeing your Wordpress designs!

People needing legal representation.

Law

Coded - Design and coding required

5+ page

Serif

• Incorporate my logo and my logo's colors.
• Live pictures and images appearing as viewers scroll on page.

```html
<!DOCTYPE html>
<html lang="en">
<head>
<meta charset="utf-8">
<title>Dorian Kessly Law</title>
<link rel="stylesheet" href="https://fonts.googleapis.com/css2?family=Playfair+Display:ital,wght@0,600;0,700;1,700&family=Poppins:wght@400;500;600&display=swap">
<style>
:root{
  --navy:#1b2536;
  --navy-deep:#121a28;
  --navy-card:#243049;
  --gold:#c4a46c;
  --gold-soft:#d8bf8f;
  --red:#cf4a31;
  --ink:#1d2230;
  --muted:#6b7280;
  --line:#e3e3e3;
  --white:#ffffff;
}
*{box-sizing:border-box;margin:0;padding:0}
html,body{width:1200px;height:3392px;overflow:hidden}
body{font-family:"Poppins",sans-serif;color:var(--ink);background:var(--white);font-size:13px;line-height:1.7}
h1,h2,h3,h4{font-family:"Playfair Display",serif;font-weight:700}
.serif-gold{color:var(--gold);font-style:italic}
.eyebrow{font-size:11px;letter-spacing:2px;text-transform:uppercase;color:var(--gold);font-weight:600}
.btn{display:inline-block;font-size:12px;font-weight:600;padding:12px 28px;color:var(--white);border:none}
.btn-red{background:var(--red)}
.btn-gold{background:var(--gold)}

/* hero block */
.hero{position:relative;height:600px;background:linear-gradient(160deg,#2a3244 0%,#1a2130 45%,#3a3a3e 100%);color:var(--white)}
.hero-shade{position:absolute;inset:0;background:rgba(18,26,40,.55)}
.topbar{position:relative;height:44px;background:var(--navy-deep);display:flex;align-items:center;padding:0 120px;font-size:11px;color:#c9ced8}
.topbar .social{display:flex;gap:8px;margin-left:24px}
.dot{width:16px;height:16px;border-radius:50%;background:#3a4560;display:inline-block}
.topbar .links{margin-left:auto;display:flex;gap:22px;align-items:center}
.topbar .quote{background:var(--gold);color:var(--navy-deep);padding:0 18px;height:44px;line-height:44px;font-weight:600}
.header{position:relative;height:92px;display:flex;align-items:center;padding:0 120px}
.brand{display:flex;align-items:center;gap:12px}
.brand-mark{width:34px;height:34px;background:var(--gold)}
.brand-name{font-family:"Playfair Display",serif;font-size:17px;letter-spacing:1px;color:var(--gold-soft);font-weight:700;line-height:1.2}
.brand-sub{font-family:"Playfair Display",serif;font-size:9px;color:var(--gold-soft);letter-spacing:1px;font-weight:700}
.contacts{margin-left:auto;display:flex;gap:34px}
.contact-item{display:flex;gap:10px;align-items:center;font-size:12px}
.contact-item small{display:block;font-size:10px;color:#b8bfcc}
.icon-ring{width:32px;height:32px;border-radius:50%;border:1px solid var(--gold);display:flex;align-items:center;justify-content:center}
.nav{position:relative;margin:0 120px;height:50px;background:var(--white);border-radius:4px;display:flex;align-items:center;padding:0 24px;gap:34px;font-size:12px;color:var(--ink);font-weight:500}
.nav .active{border:1px solid var(--line);padding:6px 14px;margin-left:-14px}
.nav .search{margin-left:auto;width:200px;height:32px;border:1px solid var(--line);display:flex;align-items:center;gap:8px;padding:0 10px;color:var(--muted);font-weight:400}
.hero-copy{position:relative;text-align:center;margin-top:66px}
.hero-title{display:flex;align-items:center;justify-content:center;gap:22px;font-size:56px;line-height:1.1}
.hero-title::before,.hero-title::after{content:"";width:90px;height:2px;background:var(--white)}
.hero-areas{font-size:13px;margin-top:12px;letter-spacing:.5px}
.hero-lead{font-size:11px;color:#cfd4dd;width:460px;margin:10px auto 28px;line-height:1.6}

/* about */
.about{height:300px;text-align:center;padding-top:58px}
.about h2{font-size:32px;margin:8px 0 16px}
.about p{width:880px;margin:0 auto;color:var(--muted);font-size:12px}

/* practice */
.practice{position:relative;height:680px;background:linear-gradient(180deg,#1e2839,#172031);color:var(--white);text-align:center;padding-top:58px}
.practice h2{font-size:32px;line-height:1.3;width:560px;margin:8px auto 40px}
.cards{display:grid;grid-template-columns:repeat(3,228px);gap:14px;justify-content:center}
.card{height:214px;background:var(--navy-card);padding:26px 22px;text-align:center}
.card.featured{background:linear-gradient(160deg,#5c5346,#2f3441)}
.card.media{background:linear-gradient(150deg,#3d4556,#1f2736);padding:0;position:relative}
.card-icon{width:44px;height:44px;margin:0 auto 12px;border:1px solid var(--gold);display:flex;align-items:center;justify-content:center}
.card h3{font-size:17px;margin-bottom:8px}
.card p{font-size:11px;color:#b9c0cc;line-height:1.6}
.card .more{display:inline-block;margin-top:12px;font-size:11px;font-weight:600}
.card.media .more{position:absolute;left:0;right:0;bottom:14px;font-family:"Playfair Display",serif;font-size:15px}

/* experience */
.experience{position:relative;height:790px;padding:90px 0 0 120px}
.experience .eyebrow{color:var(--gold)}
.experience h2{font-size:32px;margin:6px 0 16px;width:460px;line-height:1.25}
.experience p{width:470px;color:var(--muted);font-size:12px;margin-bottom:16px}
.checks{display:grid;grid-template-columns:230px 230px;gap:6px 20px;margin:8px 0 34px;font-size:12px}
.checks li{list-style:none;display:flex;gap:8px;align-items:center}
.signoff{display:flex;align-items:center;gap:40px}
.signature{width:90px;height:40px;background:linear-gradient(90deg,#e8e1d2,#f6f2ea)}
.signoff h4{font-size:17px}
.signoff small{color:var(--muted);font-size:11px}
.gold-block{position:absolute;right:0;bottom:0;width:240px;height:200px;background:var(--gold)}
.portrait{position:absolute;left:700px;top:110px;width:300px;height:680px;background:linear-gradient(180deg,#d9dbe0 0%,#2e3340 55%,#1a1d25 100%);border-radius:140px 140px 0 0}

/* contact band */
.contact-band{position:relative;height:430px;background:linear-gradient(110deg,#2b2620 0%,#1c2231 40%,#18202f 100%);color:var(--white);padding:60px 120px;display:flex;gap:80px}
.contact-band .intro{width:360px;padding-top:20px}
.contact-band h2{font-size:32px;line-height:1.25;margin:8px 0 16px}
.contact-band p{font-size:11px;color:#c5cad3}
.form{width:520px;display:grid;grid-template-columns:1fr 1fr;gap:14px}
.field{height:42px;background:var(--white);font-size:11px;color:var(--muted);padding:12px 14px}
.field.area{grid-column:1/3;height:120px}
.form .btn{width:140px}

/* footer */
.footer{position:relative;height:592px;background:var(--navy);color:#c9ced8;padding:56px 120px 0;display:flex;gap:60px}
.footer h3{color:var(--white);font-size:20px;margin-bottom:18px}
.f-col{font-size:11px}
.f-contact{width:260px}
.f-contact p{margin-bottom:14px}
.f-line{display:flex;gap:10px;align-items:center;margin-bottom:12px}
.f-phone{font-size:26px;color:var(--white);font-weight:500;margin-top:8px}
.f-form{width:260px;display:flex;flex-direction:column;gap:12px;padding-top:50px}
.f-field{height:38px;background:#243049;padding:10px 12px}
.f-form .btn{align-self:flex-start;margin-top:6px}
.f-side{width:280px}
.quick{display:grid;grid-template-columns:1fr 1fr;gap:8px 20px;margin-bottom:40px}
.quick span::before{content:"› ";color:var(--gold)}
.news{display:flex;margin-top:14px}
.news .f-field{flex:1}
.news .btn{padding:10px 16px}
.bottom{position:absolute;left:0;right:0;bottom:0;height:100px;border-top:1px solid #2f3a50;display:flex;align-items:center;padding:0 120px;font-size:11px}
.bottom .mid{margin:0 auto;display:flex;align-items:center;gap:10px}
.bottom .mid .brand-mark{width:26px;height:26px}
.badge{width:40px;height:40px;border-radius:50%;background:var(--gold);margin-right:18px}
.bottom .social{display:flex;gap:8px}
.bottom .social .dot{width:24px;height:24px;border:1px solid #55617a;background:none}
</style>
</head>
<body>

<section class="hero" role="img" aria-label="Dark photo of a courtroom gavel and scales of justice">
  <div class="hero-shade"></div>
  <div class="topbar">
    <span>Landlord Appointment</span>
    <span class="social"><i class="dot"></i><i class="dot"></i><i class="dot"></i><i class="dot"></i></span>
    <div class="links"><span>Make a Claim</span><span>Services</span><span>Practice Center</span><span class="quote">Get A Quote</span></div>
  </div>
  <div class="header">
    <div class="brand">
      <span class="brand-mark"></span>
      <div><div class="brand-name">DORIAN KESSLY LAW</div><div class="brand-sub">A PROFESSIONAL CORPORATION</div></div>
    </div>
    <div class="contacts">
      <div class="contact-item"><span class="icon-ring"><svg width="14" height="14" viewBox="0 0 24 24" fill="none" stroke="#c4a46c" stroke-width="2"><rect x="3" y="5" width="18" height="14"/><path d="M3 6l9 7 9-7"/></svg></span><div>info@example.com<small>Send us a mail</small></div></div>
      <div class="contact-item"><span class="icon-ring"><svg width="14" height="14" viewBox="0 0 24 24" fill="none" stroke="#c4a46c" stroke-width="2"><path d="M5 3h4l2 5-3 2a11 11 0 006 6l2-3 5 2v4a2 2 0 01-2 2A17 17 0 013 5a2 2 0 012-2z"/></svg></span><div>+123-456-7890<small>Call us any time</small></div></div>
      <div class="contact-item"><span class="icon-ring"><svg width="14" height="14" viewBox="0 0 24 24" fill="none" stroke="#c4a46c" stroke-width="2"><path d="M12 22s7-7 7-12a7 7 0 00-14 0c0 5 7 12 7 12z"/><circle cx="12" cy="10" r="2.5"/></svg></span><div>Address<small>1420 Capitol Ave, Sacramento</small></div></div>
    </div>
  </div>
  <nav class="nav">
    <span class="active">Home</span><span>Dorian Kessly</span><span>Practice Areas</span><span>Insights</span><span>Contact Us</span>
    <span class="search"><svg width="12" height="12" viewBox="0 0 24 24" fill="none" stroke="#6b7280" stroke-width="2.5"><circle cx="11" cy="11" r="7"/><path d="M16 16l5 5"/></svg>Search Keyword</span>
  </nav>
  <div class="hero-copy">
    <h1 class="hero-title">The Best Defence</h1>
    <div class="hero-areas">Personal Injury | Workers Compensation | Sex Offence Law | General Law</div>
    <p class="hero-lead">We stand by our clients in every courtroom, offering honest advice and strong defence when it matters most.</p>
    <span class="btn btn-red">Free Case Evaluation</span>
  </div>
</section>

<section class="about">
  <div class="eyebrow">About Us</div>
  <h2>We Always Fight For Your Justice To Win</h2>
  <p>Trusted counsel for people facing hard disputes. We listen first, explain every option plainly and prepare each case as if it will go to trial. From criminal charges to business, property and employment conflicts, our practice is built on careful preparation, direct communication and a record of standing firm for ordinary people when the stakes are high and the path forward seems unclear.</p>
</section>

<section class="practice">
  <div class="eyebrow">Practice Area</div>
  <h2>We Are Here To Fight Against Any Violance With <span class="serif-gold">Experience</span></h2>
  <div class="cards">
    <div class="card"><div class="card-icon"><svg width="22" height="22" viewBox="0 0 24 24" fill="none" stroke="#c4a46c" stroke-width="1.6"><circle cx="8" cy="7" r="3"/><circle cx="16" cy="7" r="3"/><path d="M3 20v-3a5 5 0 0110 0v3M11 20v-3a5 5 0 0110 0v3"/></svg></div><h3>Family Law</h3><p>Clear guidance through custody, support and divorce matters with care.</p><span class="more">Read More ›</span></div>
    <div class="card featured"><div class="card-icon"><svg width="22" height="22" viewBox="0 0 24 24" fill="none" stroke="#c4a46c" stroke-width="1.6"><rect x="4" y="8" width="16" height="12"/><path d="M9 8V5h6v3"/></svg></div><h3>Corporate Security</h3><p>Protecting your business in contract and partnership disputes.</p><span class="more">Read More ›</span></div>
    <div class="card"><div class="card-icon"><svg width="22" height="22" viewBox="0 0 24 24" fill="none" stroke="#c4a46c" stroke-width="1.6"><path d="M12 3v18M5 21h14M4 8h16M4 8l-2 6h4zM20 8l-2 6h4z"/></svg></div><h3>Criminal Law</h3><p>Firm defence for DUI, theft, assault and drug charges in court.</p><span class="more">Read More ›</span></div>
    <div class="card"><div class="card-icon"><svg width="22" height="22" viewBox="0 0 24 24" fill="none" stroke="#c4a46c" stroke-width="1.6"><rect x="3" y="6" width="18" height="13"/><path d="M3 10h18"/></svg></div><h3>Bankruptcy Law</h3><p>Practical plans to manage debt and keep what matters to you.</p><span class="more">Read More ›</span></div>
    <div class="card"><div class="card-icon"><svg width="22" height="22" viewBox="0 0 24 24" fill="none" stroke="#c4a46c" stroke-width="1.6"><path d="M3 11l9-7 9 7M6 10v10h12V10"/></svg></div><h3>Real Estate Law</h3><p>Sound counsel on property, title and landlord tenant disputes.</p><span class="more">Read More ›</span></div>
    <div class="card media" role="img" aria-label="Photo of scales of justice on a desk"><span class="more">View More</span></div>
  </div>
</section>

<section class="experience">
  <div class="eyebrow">Lawyer Info</div>
  <h2>Ready, Reliable &amp; Experienced</h2>
  <p>Former prosecutor and seasoned civil litigator, bringing courtroom experience from both sides of the aisle to every client and every case we take on.</p>
  <p>Each matter receives personal attention from start to finish. We review the facts closely, build a clear strategy and keep you informed at every step, so you always know where your case stands and what comes next in the process.</p>
  <ul class="checks">
    <li><svg width="14" height="14" viewBox="0 0 24 24" fill="none" stroke="#c4a46c" stroke-width="3"><path d="M4 12l5 5L20 6"/></svg>Acquire free trial available</li>
    <li><svg width="14" height="14" viewBox="0 0 24 24" fill="none" stroke="#c4a46c" stroke-width="3"><path d="M4 12l5 5L20 6"/></svg>Learn from customer feedback</li>
    <li><svg width="14" height="14" viewBox="0 0 24 24" fill="none" stroke="#c4a46c" stroke-width="3"><path d="M4 12l5 5L20 6"/></svg>Engage – marketing automation</li>
    <li><svg width="14" height="14" viewBox="0 0 24 24" fill="none" stroke="#c4a46c" stroke-width="3"><path d="M4 12l5 5L20 6"/></svg>Support – customer support</li>
    <li><svg width="14" height="14" viewBox="0 0 24 24" fill="none" stroke="#c4a46c" stroke-width="3"><path d="M4 12l5 5L20 6"/></svg>Acquire free trial available</li>
    <li><svg width="14" height="14" viewBox="0 0 24 24" fill="none" stroke="#c4a46c" stroke-width="3"><path d="M4 12l5 5L20 6"/></svg>Learn from customer feedback</li>
    <li><svg width="14" height="14" viewBox="0 0 24 24" fill="none" stroke="#c4a46c" stroke-width="3"><path d="M4 12l5 5L20 6"/></svg>Engage – marketing automation</li>
    <li><svg width="14" height="14" viewBox="0 0 24 24" fill="none" stroke="#c4a46c" stroke-width="3"><path d="M4 12l5 5L20 6"/></svg>Support – customer support</li>
  </ul>
  <div class="signoff">
    <div class="signature" role="img" aria-label="Handwritten signature"></div>
    <div><h4>Dorian Kessly (M.L.B)</h4><small>Chairman Founder</small></div>
  </div>
  <div class="gold-block"></div>
  <div class="portrait" role="img" aria-label="Portrait of the attorney in a dark suit"></div>
</section>

<section class="contact-band" role="img" aria-label="Dim photo of a statue of justice behind the contact form">
  <div class="intro">
    <div class="eyebrow" style="color:#fff">Contact Us</div>
    <h2>Feel Free To Ask Send Your <span class="serif-gold">Message.</span></h2>
    <p>Tell us about your situation and we will reply within one business day to arrange a confidential review.</p>
  </div>
  <div class="form">
    <div class="field">Name</div><div class="field">Email</div>
    <div class="field">Phone</div><div class="field">Subject</div>
    <div class="field area">Message</div>
    <span class="btn btn-gold">Submit Request</span>
  </div>
</section>

<footer class="footer">
  <div class="f-col f-contact">
    <h3>Contact Info</h3>
    <p>We are always available for you to reach out to us, and we will reply as soon as we can.</p>
    <div class="f-line"><span class="icon-ring"><svg width="12" height="12" viewBox="0 0 24 24" fill="none" stroke="#c4a46c" stroke-width="2"><path d="M12 22s7-7 7-12a7 7 0 00-14 0c0 5 7 12 7 12z"/></svg></span>1420 Capitol Ave, Sacramento</div>
    <div class="f-line"><span class="icon-ring"><svg width="12" height="12" viewBox="0 0 24 24" fill="none" stroke="#c4a46c" stroke-width="2"><rect x="3" y="5" width="18" height="14"/><path d="M3 6l9 7 9-7"/></svg></span>info@example.com</div>
    <div class="f-line"><span class="icon-ring"><svg width="12" height="12" viewBox="0 0 24 24" fill="none" stroke="#c4a46c" stroke-width="2"><circle cx="12" cy="12" r="9"/><path d="M12 7v5l3 2"/></svg></span>Monday to Saturday: 9am – 6pm</div>
    <div class="f-phone">+ 123 – 456 –7890</div>
  </div>
  <div class="f-col f-form">
    <div class="f-field">Your Name</div>
    <div class="f-field">Email Address</div>
    <div class="f-field">Phone Number</div>
    <div class="f-field">Select Service</div>
    <div class="f-field" style="height:80px">Message</div>
    <span class="btn btn-gold">Submit Request</span>
  </div>
  <div class="f-col f-side">
    <h3>Quick Links</h3>
    <div class="quick"><span>Make Appointment</span><span>Criminal Case</span><span>Customer Services</span><span>Family Law</span><span>Business Law</span><span>Gaming Tool</span><span>Gaming Tool</span><span>Management Law</span><span>Personal Issues</span><span>Personal Issues</span></div>
    <h3>Newsletter</h3>
    <p>Subscribe to our newsletter to receive legal news and updates in your inbox.</p>
    <div class="news"><div class="f-field">Email Address</div><span class="btn btn-gold">›</span></div>
  </div>
  <div class="bottom">
    <div>Copyright © 2024, Dorian Kessly<br>About Us | Services | Privacy</div>
    <div class="mid"><span class="brand-mark"></span><span class="brand-name" style="font-size:13px">DORIAN KESSLY LAW</span></div>
    <span class="badge"></span>
    <div class="social"><i class="dot"></i><i class="dot"></i><i class="dot"></i></div>
  </div>
</footer>

</body>
</html>
```